Cascadia Rhythm Guild Business Cards

The Cascadia Rhythm Guild is a non-profit organization that supports, promotes, and manages music events in the Pacific Northwest. Our mission is to keep the blues alive. We do this by partnering with local venues, schools, and national acts to bring some of the best blues music to our members. As newly elected Executive Board Members we would like to have new business cards designed. I have included a copy of our logo.

```html
<!DOCTYPE html>
<html lang="en">
<head>
<meta charset="utf-8">
<title>Cascadia Rhythm Guild Business Cards</title>
<link href="https://fonts.googleapis.com/css2?family=Montserrat:wght@400;500;700&display=swap" rel="stylesheet">
<style>
  :root {
    --stage: #1c1c1f;
    --card-white: #ffffff;
    --ink: #1a1a1a;
    --brand-blue: #4a8fd6;
    --band-blue: #6a9fd8;
    --stripe-orange: #e8702a;
    --stripe-red: #c8202f;
    --badge-yellow: #f3e98a;
    --stage-indigo: #2b2f8f;
    --stage-violet: #5a3aa0;
    --stage-cyan: #3aa6e0;
  }
  * { box-sizing: border-box; margin: 0; padding: 0; }
  html, body { width: 1200px; height: 900px; overflow: hidden; }
  body {
    background: var(--stage);
    font-family: "Montserrat", sans-serif;
    position: relative;
  }
  .card {
    position: absolute;
    left: 270px;
    width: 660px;
    height: 377px;
    border-radius: 22px;
    overflow: hidden;
  }
  .card-front { top: 40px; background: var(--card-white); }
  .card-back { top: 463px; }

  .front-bands { position: absolute; inset: 0; }

  .brand-lockup {
    position: absolute;
    left: 48px;
    top: 100px;
    display: flex;
    align-items: center;
    gap: 14px;
  }
  .brand-dot {
    width: 70px; height: 70px;
    border-radius: 50%;
    background: var(--badge-yellow);
    flex: none;
  }
  .brand-name {
    font-weight: 700;
    font-size: 26px;
    line-height: 1.15;
    color: var(--brand-blue);
    white-space: nowrap;
  }

  .divider-lines { position: absolute; left: 350px; top: 120px; }

  .contact {
    position: absolute;
    left: 422px;
    top: 130px;
    color: var(--ink);
    font-size: 14px;
    line-height: 1.35;
  }
  .contact-name {
    font-weight: 700;
    font-size: 18px;
    letter-spacing: 1.5px;
    color: var(--brand-blue);
    text-transform: uppercase;
  }
  .contact-role { font-size: 15px; margin-bottom: 8px; }
  .contact-address { margin-bottom: 8px; }
  .contact-row { display: flex; align-items: center; gap: 8px; }
  .contact-icon { width: 14px; height: 14px; flex: none; }

  .back-photo {
    position: absolute; inset: 0;
    background:
      radial-gradient(circle at 70% 20%, var(--stage-cyan) 0, transparent 30%),
      radial-gradient(circle at 20% 70%, var(--stage-violet) 0, transparent 45%),
      linear-gradient(135deg, var(--stage-indigo), var(--stage-violet));
  }
  .back-lockup {
    position: absolute;
    left: 330px;
    top: 120px;
    display: flex;
    align-items: center;
    gap: 16px;
  }
  .back-lockup .brand-name { color: var(--badge-yellow); font-size: 30px; }
</style>
</head>
<body>

<section class="card card-front">
  <svg class="front-bands" width="660" height="377" viewBox="0 0 660 377" aria-hidden="true">
    <defs>
      <linearGradient id="stripeGrad" x1="0" y1="0" x2="1" y2="0">
        <stop offset="0" stop-color="var(--stripe-orange)"/>
        <stop offset="1" stop-color="var(--stripe-red)"/>
      </linearGradient>
    </defs>
    <path d="M0,278 L345,322 L330,327 L0,296 Z" fill="url(#stripeGrad)"/>
    <path d="M0,300 L330,327 C385,332 430,350 470,377 L0,377 Z" fill="var(--band-blue)"/>
  </svg>

  <div class="brand-lockup">
    <span class="brand-dot"></span>
    <span class="brand-name">Cascadia<br>Rhythm Guild</span>
  </div>

  <svg class="divider-lines" width="60" height="150" viewBox="0 0 60 150" aria-hidden="true">
    <line x1="40" y1="0" x2="2" y2="150" stroke="var(--brand-blue)" stroke-width="1.5"/>
    <line x1="58" y1="0" x2="20" y2="150" stroke="var(--brand-blue)" stroke-width="1.5"/>
  </svg>

  <div class="contact">
    <p class="contact-name">Marcus Delaney</p>
    <p class="contact-role">Co-Founder</p>
    <p class="contact-address">2840 Alder Street, Ste<br>210, Tacoma, WA 98402</p>
    <p class="contact-row">
      <svg class="contact-icon" viewBox="0 0 14 14" aria-hidden="true"><path d="M3 1 L5 1 L6 4 L4.5 5 Q5.5 7.5 9 9.5 L10 8 L13 9 L13 11 Q12 13 10 13 Q2 11 1 3 Q1 1 3 1 Z" fill="var(--brand-blue)"/></svg>
      555-014-2368
    </p>
    <p class="contact-row">
      <svg class="contact-icon" viewBox="0 0 14 14" aria-hidden="true"><rect x="1" y="3" width="12" height="8" fill="var(--brand-blue)"/><path d="M1 3 L7 8 L13 3" stroke="#fff" fill="none" stroke-width="1"/></svg>
      hello@cascadiarhythm.org
    </p>
    <p class="contact-row">
      <svg class="contact-icon" viewBox="0 0 14 14" aria-hidden="true"><circle cx="7" cy="7" r="6" fill="var(--brand-blue)"/><path d="M1 7 H13 M7 1 Q3 7 7 13 Q11 7 7 1" stroke="#fff" fill="none" stroke-width="0.8"/></svg>
      www.cascadiarhythm.org
    </p>
  </div>
</section>

<section class="card card-back">
  <div class="back-photo" role="img" aria-label="Newsletter cover photo: blues musicians on a blue-lit stage with the newsletter title and issue date"></div>
  <div class="back-lockup">
    <span class="brand-dot"></span>
    <span class="brand-name">Cascadia<br>Rhythm Guild</span>
  </div>
</section>

</body>
</html>
```